Rebrand of 3 bottle labels for nail polish brand

The task is to make a rebranding of our current gel nail polish bottle design. We have become one of the leading european nail polish brand, so we want to improve the quality of the label design to a more scandinavian and minimalistic bottle design, which stille has to be recognisable and unique.

We have attached a more detailed description of the rebranding instructions for our gel polish bottles called "bottle task".
Updates

The Labels should not be just Black and White as stated. But should be mainly Black and White and then some of our color as explained in the uploaded file.

Target Market(s)

Girls and women age 18-55 Northern Europe

Industry/Entity Type

Cosmetic/ Nail Gel Polish

Colors

Designer to choose only greyscale colors for use in the design.

Requirements
Must have
• See attched design instruction
Nice to have
• Moderne, Minimalist, Recognizable and Unique look
Should not have
• Too many elements, too busy design

```html
<!DOCTYPE html>
<html lang="en">
<head>
<meta charset="utf-8">
<title>Velmora Gel Polish Labels</title>
<link rel="stylesheet" href="https://fonts.googleapis.com/css2?family=Montserrat:wght@600;800&family=Playfair+Display:ital,wght@0,400;0,900;1,400&family=Poppins:wght@400&display=swap">
<style>
  :root {
    --backdrop: #d9d9d9;
    --bottle: #0b0b0b;
    --label: #151515;
    --cap-shine: #222222;
    --white: #ffffff;
    --rose: #b98f87;
    --berry: #e8344a;
    --sea: #5cc79a;
  }
  * { margin: 0; padding: 0; box-sizing: border-box; }
  html, body { width: 1200px; height: 800px; overflow: hidden; }
  body {
    background: var(--backdrop);
    position: relative;
    font-family: "Poppins", sans-serif;
    color: var(--white);
  }
  .bottle { position: absolute; top: 274px; width: 158px; height: 382px; }
  .bottle-cap {
    position: absolute; left: 27px; top: 0; width: 104px; height: 199px;
    background: linear-gradient(90deg, var(--bottle) 0%, var(--cap-shine) 45%, var(--bottle) 100%);
    border-radius: 18px 18px 2px 2px;
  }
  .bottle-base {
    position: absolute; left: 0; top: 199px; width: 158px; height: 183px;
    background: var(--label);
    border-radius: 14px 14px 22px 22px;
    text-align: center;
    padding-top: 27px;
  }
  .brand-name {
    font-family: "Montserrat", sans-serif;
    font-weight: 600;
    color: var(--white);
    line-height: 1;
    letter-spacing: 3px;
    text-transform: uppercase;
  }
  .bottle .brand-name { font-size: 17px; }
  .coat-type {
    font-family: "Montserrat", sans-serif; font-weight: 800;
    font-size: 11px; letter-spacing: 0.4px; margin-top: 14px;
  }
  .cure-note {
    font-family: "Playfair Display", serif; font-weight: 400;
    font-size: 7.5px; letter-spacing: 0.3px; margin-top: 3px;
  }
  .shade-number {
    font-family: "Playfair Display", serif; font-weight: 900;
    font-size: 42px; line-height: 1; margin-top: 3px;
  }
  .shade-name {
    font-family: "Playfair Display", serif; font-style: italic;
    font-size: 11px; line-height: 1;
  }
  .vegan-note { font-size: 9.5px; margin-top: 9px; letter-spacing: 0.2px; }
  .shade-berry { color: var(--berry); }
  .shade-sea { color: var(--sea); }
  .shade-base { color: var(--rose); }

  .bottle-berry { left: 151px; }
  .bottle-sea { left: 332px; }
  .bottle-steady { left: 603px; }

  .remover {
    position: absolute; left: 892px; top: 122px; width: 184px; height: 534px;
  }
  .remover-cap {
    position: absolute; inset: 0 0 auto 0; height: 132px;
    background: var(--bottle);
    border-radius: 22px 22px 0 0;
  }
  .remover-body {
    position: absolute; left: 0; top: 132px; width: 184px; height: 402px;
    background: var(--label);
    border-radius: 0 0 14px 14px;
    text-align: center;
    padding-top: 74px;
  }
  .remover .brand-name { font-size: 27px; letter-spacing: 4px; }
  .remover-title {
    font-family: "Montserrat", sans-serif; font-weight: 800;
    font-size: 19px; line-height: 1.3; margin-top: 28px; letter-spacing: 0.3px;
  }
  .remover-number {
    font-family: "Playfair Display", serif; font-weight: 900;
    font-size: 84px; line-height: 1; color: var(--rose); margin-top: 26px;
  }
  .remover-volume {
    font-family: "Montserrat", sans-serif; font-weight: 600;
    font-size: 13.5px; margin-top: 44px;
  }
</style>
</head>
<body>
  <div class="bottle bottle-berry">
    <div class="bottle-cap"></div>
    <div class="bottle-base" role="img" aria-label="Label with subtle tonal leaf pattern">
      <div class="brand-name">Velmora</div>
      <div class="coat-type">COLOR COAT</div>
      <div class="cure-note">SOAK OFF UV/LED</div>
      <div class="shade-number shade-berry">27</div>
      <div class="shade-name shade-berry">Cherry Note</div>
      <div class="vegan-note">Vegan Formula</div>
    </div>
  </div>

  <div class="bottle bottle-sea">
    <div class="bottle-cap"></div>
    <div class="bottle-base" role="img" aria-label="Label with subtle tonal leaf pattern">
      <div class="brand-name">Velmora</div>
      <div class="coat-type">COLOR COAT</div>
      <div class="cure-note">SOAK OFF UV/LED</div>
      <div class="shade-number shade-sea">203</div>
      <div class="shade-name shade-sea">Sea Glass</div>
      <div class="vegan-note">Vegan Formula</div>
    </div>
  </div>

  <div class="bottle bottle-steady">
    <div class="bottle-cap"></div>
    <div class="bottle-base" role="img" aria-label="Label with subtle tonal leaf pattern">
      <div class="brand-name">Velmora</div>
      <div class="coat-type">BASE COAT</div>
      <div class="cure-note">SOAK OFF UV/LED</div>
      <div class="shade-number shade-base">05</div>
      <div class="shade-name shade-base">Steady</div>
      <div class="vegan-note">Vegan Formula</div>
    </div>
  </div>

  <div class="remover">
    <div class="remover-cap"></div>
    <div class="remover-body" role="img" aria-label="Remover label with subtle tonal leaf pattern">
      <div class="brand-name">Velmora</div>
      <div class="remover-title">GEL POLISH<br>REMOVER</div>
      <div class="remover-number">09</div>
      <div class="remover-volume">120ml · 4 fl.oz</div>
    </div>
  </div>
</body>
</html>
```